Business Card Design for Flood Rescue 360 - Property Restoration Professionals

I need a business card designed for Flood Rescue 360. We are a full-service property restoration solution. Providing water, fire, smoke & storm restoration as well as mold remediation and full remodel or reconstruction to homes and businesses across Dallas-Fort Worth, TX.
Target Market(s)
home and business owners with insurance covered property damage from water, fire or storm related damage
Industry/Entity Type
property restoration
Contact Information for Business Card
Martin Kell General Manager Cell: 214-555-0193 Office: 469-555-0148 email: Martin@FloodRescue360.example services: Water, Fire, Mold, Reconstruction Tagline: Urgency for Your Water Emergency!
Look and feel
Each slider illustrates characteristics of the customer's brand and the style your logo design should communicate.

```html
<!DOCTYPE html>
<html lang="en">
<head>
<meta charset="utf-8">
<title>Flood Rescue 360 – Business Card</title>
<link rel="stylesheet" href="https://fonts.googleapis.com/css2?family=Roboto:wght@400;500;700&display=swap">
<style>
  :root {
    --backdrop: #0f5369;
    --cyan: #4af4f4;
    --grey: #636e70;
    --white: #ffffff;
  }
  * { margin: 0; padding: 0; box-sizing: border-box; }
  html, body { width: 1067px; height: 1200px; overflow: hidden; background: var(--backdrop); }
  body { position: relative; font-family: "Roboto", Arial, sans-serif; }

  .card {
    position: absolute;
    left: 67px;
    width: 932px;
    height: 533px;
    border-radius: 49px;
    overflow: hidden;
  }
  .card--front { top: 47px; background: var(--white); }
  .card--back { top: 620px; background: var(--cyan); }

  .card__bands { position: absolute; inset: 0; width: 100%; height: 100%; }

  .brand {
    position: absolute;
    display: flex;
    align-items: center;
    gap: 14px;
    font-weight: 700;
    line-height: 0.95;
    letter-spacing: 0.3px;
    white-space: nowrap;
  }
  .brand__name { font-size: 42px; }
  .brand__mark { width: 66px; height: 66px; border-radius: 50%; border: 7px solid currentColor; flex: none; }
  .card--front .brand { left: 110px; top: 204px; color: var(--cyan); }
  .card--back .brand { right: 33px; top: 392px; color: var(--white); }

  .person { position: absolute; left: 533px; top: 74px; }
  .person__name { font-size: 31px; font-weight: 700; color: var(--grey); letter-spacing: 0.5px; }
  .person__first { color: var(--cyan); }
  .person__title { font-size: 19.5px; color: var(--grey); margin-top: 4px; }

  .contact { position: absolute; left: 533px; top: 320px; list-style: none; font-size: 23px; color: var(--grey); }
  .contact li { height: 31px; line-height: 31px; white-space: nowrap; }
  .contact__label { color: var(--cyan); margin-right: 8px; }
  .contact__user { color: var(--cyan); }

  .tagline, .services {
    position: absolute;
    color: var(--white);
    font-weight: 500;
    white-space: nowrap;
  }
  .tagline { left: 48px; top: 503px; font-size: 19.5px; letter-spacing: 0.3px; }
  .services { left: 534px; top: 491px; font-size: 17px; letter-spacing: 0.2px; }
</style>
</head>
<body>

<section class="card card--front" aria-label="Card front">
  <svg class="card__bands" viewBox="0 0 1049 600" preserveAspectRatio="none" aria-hidden="true">
    <polygon points="0,546 560,546 598,584 1049,584 1049,546" fill="var(--grey)"/>
    <polygon points="0,546 560,546 560,553 0,553" fill="var(--grey)"/>
    <polygon points="0,561 552,561 592,592 1049,592 1049,600 0,600" fill="var(--cyan)"/>
  </svg>

  <div class="brand">
    <span class="brand__name">FLOOD<br>RESCUE 360</span>
    <span class="brand__mark"></span>
  </div>

  <div class="person">
    <h1 class="person__name"><span class="person__first">MARTIN</span> KELL</h1>
    <p class="person__title">General Manager</p>
  </div>

  <ul class="contact">
    <li><span class="contact__label">C:</span>214-555-0193</li>
    <li><span class="contact__label">O:</span>469-555-0148</li>
    <li><span class="contact__user">Martin@</span>FloodRescue360.example</li>
  </ul>

  <p class="services">WATER, FIRE, MOLD, RECONSTRUCTION</p>
  <p class="tagline">URGENCY FOR YOUR WATER EMERGENCY!</p>
</section>

<section class="card card--back" aria-label="Card back">
  <svg class="card__bands" viewBox="0 0 1049 600" preserveAspectRatio="none" aria-hidden="true">
    <rect x="0" y="582" width="1049" height="5" fill="var(--white)"/>
  </svg>
  <div class="brand">
    <span class="brand__name">FLOOD<br>RESCUE 360</span>
    <span class="brand__mark"></span>
  </div>
</section>

</body>
</html>
```